Two Versions of a Business Card for a Lawyer

Summary: I need a logo and a business card. The business card is two-sided and comes in two versions. One version is conservative, the other is slightly different with one or more pink embellishments in the logo or somewhere else in the business card.
I'm about to start off as a sole practitioner in criminal and immigration law. I'll largely be working with marginalised communities and in areas of social justice. One of my main focuses will be gendered violence, I'm hoping to specialise my practice towards representing victims of domestic and sexual violence and sex workers. I want a business card which would attract this clientele and make them feel safe to speak with me. I'd also like it to communicate a sense of hope.
However, the business card still has to be very conservative as the legal profession is very stuffy. So I was thinking of having two versions of the same card, one would be very straight forward while the other would have a **pink embellishment** or perhaps several. For example, if the scales of justice were used in the design, maybe the second version would have a pink flower about to bloom on the scale somewhere. Or maybe it's my logo that is different and pink.
While both designs have to be pretty conservative, I still want it to give off a sense that I'm alternative and think outside the box. With lawyers, I think a little bit of deviation goes a long way (less is more).
As far as colour goes (other than the pink embellishment), I was thinking something monochromatic, probably black and white but I am open to considering more colours. I personally love colour, and would love to use more colour, but am hesitant because of the nature of the profession. If you can find a way to use more colour while keeping it conservative and letting the pink pop, I'd be pretty pleased.
In general, I would prefer a clean simplistic design and logo. It should be immediately obvious that I'm a lawyer just by glancing at the card. I'm open to symbols of law, like the scales of justice or lady justice or something else. However, I don't want it to be the same as everyone else's.
Eventually, the design/style should be easy to recreate in the form of a website.
As far as the logo goes, it would probably use a circle as my last name starts with the letter "O". It can be very simple, with just my name and "Barrister & Solicitor". I don't currently have a logo, but the winning designer will be invited to provide a separate file for just the logo for an additional fee (I think it was CA$99). (Please ignore the uploaded logo file, it just wouldn't let me continue without uploading something).
As for the information that should go into the card, I'm still finalizing my address and phone number. So please use a placeholder for now.
Target Market(s)
Women, victims of sexual or domestic violence, refugees, people in need of legal services
Industry/Entity Type
Lawyer
Contact Information for Business Card
Maren Vickery
Barrister & Solicitor
LL.B., B.C.L., B.F.A.
Criminal & Immigration Law
Street address
Toronto, ON
Postal Code
Phone number
Fax number
Email
Logo Text
Maren Vickery, Barrister & Solicitor
Requirements
Must have
- Two versions
- One with pink
- Simplistic
Nice to have
- Maybe more colour
Should not have
- Not too conservative
- Not too predictable

```html
<!DOCTYPE html>
<html lang="en">
<head>
<meta charset="utf-8">
<title>Maren Vickery – Business Card Versions</title>
<link href="https://fonts.googleapis.com/css2?family=Cinzel:wght@700;900&family=Ubuntu:wght@500&family=Carlito&display=swap" rel="stylesheet">
<style>
  :root {
    --backdrop: #2f3739;
    --paper: #ffffff;
    --pink: #ee2eea;
    --plum: #3b1548;
    --plum-ink: #2a0f38;
    --plum-soft: #7a4f8a;
    --plum-rule: #6b5a78;
    --slate: #4f5f5e;
    --black: #050505;
    --grey-ink: #4a5858;
  }
  * { margin: 0; padding: 0; box-sizing: border-box; }
  html, body {
    width: 1200px; height: 811px; overflow: hidden;
    background: var(--backdrop);
  }
  .sheet { position: relative; width: 1200px; height: 811px; }

  .card-set {
    position: absolute; left: 30px; width: 1140px; height: 360px;
    background: var(--paper);
  }
  .card-set--pink { top: 31px;
    --band: var(--pink); --stripe: var(--plum); --gap: var(--paper);
    --ink: var(--plum-ink); --tag: var(--plum-soft); --rule-left: var(--pink);
    --rule-right: var(--plum-rule); --detail: var(--plum-ink); --icon: var(--pink);
    --seal: var(--pink); }
  .card-set--mono { top: 424px;
    --band: var(--slate); --stripe: var(--black); --gap: var(--backdrop);
    --ink: var(--black); --tag: var(--grey-ink); --rule-left: var(--pink);
    --rule-right: var(--pink); --detail: var(--grey-ink); --icon: var(--grey-ink);
    --seal: var(--slate); }

  .band, .stripe, .gap { position: absolute; top: 0; height: 100%; }
  .band { background: var(--band); }
  .stripe { background: var(--stripe); }
  .gap { background: var(--gap); }

  .seal { position: absolute; border-radius: 50%; background: var(--seal); }
  .seal--front { left: 204px; top: 71px; width: 130px; height: 130px; }
  .seal--back { left: 1005px; top: 219px; width: 102px; height: 102px;
    border: 3px solid var(--paper); }

  .name {
    position: absolute; white-space: nowrap;
    font-family: "Cinzel", serif; font-weight: 900; color: var(--ink);
    letter-spacing: 1px; line-height: 1;
  }
  .name--front { left: 120px; width: 301px; top: 222px; font-size: 33px; text-align: center; }
  .name--back { right: 114px; top: 21px; font-size: 36px; text-align: right; }

  .rule { position: absolute; height: 2px; }
  .rule--front { left: 137px; width: 267px; top: 262px; background: var(--rule-left); }
  .rule--back { left: 719px; width: 307px; top: 70px; background: var(--rule-right); }

  .tagline {
    position: absolute; left: 120px; width: 301px; top: 268px; text-align: center;
    font-family: "Ubuntu", sans-serif; font-weight: 500; font-size: 16.5px;
    line-height: 20px; letter-spacing: 2px; color: var(--tag);
  }
  .practice {
    position: absolute; right: 114px; top: 83px;
    font-family: "Ubuntu", sans-serif; font-weight: 500; font-size: 20px;
    line-height: 24px; letter-spacing: 2px; color: var(--ink); white-space: nowrap;
  }
  .credentials {
    position: absolute; right: 114px; top: 121px;
    font-family: "Carlito", sans-serif; font-size: 14px; line-height: 18px;
    color: var(--detail); white-space: nowrap;
  }

  .contact { position: absolute; left: 720px; width: 320px; height: 36px; }
  .contact__icon {
    position: absolute; left: 6px; top: 50%; transform: translateY(-50%);
    width: 30px; height: 26px; display: flex; align-items: center; justify-content: center;
    color: var(--icon);
  }
  .contact__icon svg { width: 30px; height: 24px; }
  .contact__at { font-family: "Carlito", sans-serif; font-size: 30px; line-height: 1; }
  .contact__text {
    position: absolute; left: 50px; right: 70px; top: 50%; transform: translateY(-50%);
    text-align: center; font-family: "Carlito", sans-serif; font-size: 17px;
    line-height: 20px; color: var(--detail); white-space: nowrap;
  }
  .contact--address { top: 175px; height: 40px; }
  .contact--address .contact__icon { top: 8px; }
  .contact--phone { top: 222px; }
  .contact--fax { top: 262px; }
  .contact--email { top: 301px; }
</style>
</head>
<body>
<main class="sheet">

  <section class="card-set card-set--pink" aria-label="Pink version, front and back">
    <div class="band" style="left:0;width:51px"></div>
    <div class="stripe" style="left:56px;width:10.5px"></div>
    <div class="stripe" style="left:471px;width:9.5px"></div>
    <div class="band" style="left:487px;width:50px"></div>
    <div class="gap" style="left:537px;width:65px"></div>
    <div class="band" style="left:602px;width:52px"></div>
    <div class="stripe" style="left:658px;width:10.5px"></div>
    <div class="stripe" style="left:1072px;width:10px"></div>
    <div class="band" style="left:1088px;width:52px"></div>

    <div class="seal seal--front" role="img" aria-label="Circular emblem"></div>
    <h1 class="name name--front">Maren Vickery</h1>
    <div class="rule rule--front"></div>
    <p class="tagline">Barrister &amp; Solicitor</p>

    <h2 class="name name--back">Maren Vickery</h2>
    <div class="rule rule--back"></div>
    <p class="practice">Criminal &amp; Immigration Law</p>
    <p class="credentials">LL.B., B.C.L., B.F.A.</p>

    <div class="contact contact--address">
      <span class="contact__icon"><svg viewBox="0 0 30 22"><rect x="1" y="1" width="28" height="20" fill="currentColor"/><path d="M1 1 L15 13 L29 1" fill="none" stroke="#fff" stroke-width="2"/></svg></span>
      <span class="contact__text">Street address, Toronto, ON<br>Postal Code</span>
    </div>
    <div class="contact contact--phone">
      <span class="contact__icon"><svg viewBox="0 0 32 26"><path d="M3 3h16a2 2 0 0 1 2 2v8a2 2 0 0 1-2 2H10l-5 4v-4H3a2 2 0 0 1-2-2V5a2 2 0 0 1 2-2z" fill="#fff" stroke="currentColor" stroke-width="1.6"/><path d="M14 9h14a2 2 0 0 1 2 2v8a2 2 0 0 1-2 2h-1v4l-5-4h-8a2 2 0 0 1-2-2v-8a2 2 0 0 1 2-2z" fill="#fff" stroke="currentColor" stroke-width="1.6"/><circle cx="18" cy="15" r="1" fill="currentColor"/><circle cx="21.5" cy="15" r="1" fill="currentColor"/><circle cx="25" cy="15" r="1" fill="currentColor"/></svg></span>
      <span class="contact__text">+00 000 000 0000</span>
    </div>
    <div class="contact contact--fax">
      <span class="contact__icon"><svg viewBox="0 0 30 26"><rect x="8" y="1" width="14" height="8" fill="#fff" stroke="currentColor" stroke-width="1.6"/><rect x="2" y="8" width="26" height="13" rx="3" fill="#fff" stroke="currentColor" stroke-width="1.6"/><rect x="7" y="15" width="16" height="10" fill="#fff" stroke="currentColor" stroke-width="1.6"/><path d="M10 18h10M10 21h10" stroke="currentColor" stroke-width="1.4"/></svg></span>
      <span class="contact__text">+00 000 000 0000</span>
    </div>
    <div class="contact contact--email">
      <span class="contact__icon"><span class="contact__at">@</span></span>
      <span class="contact__text">maren@maren-vickery.com</span>
    </div>

    <div class="seal seal--back" role="img" aria-label="Circular emblem"></div>
  </section>

  <section class="card-set card-set--mono" aria-label="Monochrome version, front and back">
    <div class="band" style="left:0;width:51px"></div>
    <div class="stripe" style="left:56px;width:10.5px"></div>
    <div class="stripe" style="left:471px;width:9.5px"></div>
    <div class="band" style="left:487px;width:50px"></div>
    <div class="gap" style="left:537px;width:65px"></div>
    <div class="band" style="left:602px;width:52px"></div>
    <div class="stripe" style="left:658px;width:10.5px"></div>
    <div class="stripe" style="left:1072px;width:10px"></div>
    <div class="band" style="left:1088px;width:52px"></div>

    <div class="seal seal--front" role="img" aria-label="Circular emblem"></div>
    <h1 class="name name--front">Maren Vickery</h1>
    <div class="rule rule--front"></div>
    <p class="tagline">Barrister &amp; Solicitor</p>

    <h2 class="name name--back">Maren Vickery</h2>
    <div class="rule rule--back"></div>
    <p class="practice">Criminal &amp; Immigration Law</p>
    <p class="credentials">LL.B., B.C.L., B.F.A.</p>

    <div class="contact contact--address">
      <span class="contact__icon"><svg viewBox="0 0 30 22"><rect x="1" y="1" width="28" height="20" fill="currentColor"/><path d="M1 1 L15 13 L29 1" fill="none" stroke="#fff" stroke-width="2"/></svg></span>
      <span class="contact__text">Street address, Toronto, ON<br>Postal Code</span>
    </div>
    <div class="contact contact--phone">
      <span class="contact__icon"><svg viewBox="0 0 32 26"><path d="M3 3h16a2 2 0 0 1 2 2v8a2 2 0 0 1-2 2H10l-5 4v-4H3a2 2 0 0 1-2-2V5a2 2 0 0 1 2-2z" fill="#fff" stroke="currentColor" stroke-width="1.6"/><path d="M14 9h14a2 2 0 0 1 2 2v8a2 2 0 0 1-2 2h-1v4l-5-4h-8a2 2 0 0 1-2-2v-8a2 2 0 0 1 2-2z" fill="#fff" stroke="currentColor" stroke-width="1.6"/><circle cx="18" cy="15" r="1" fill="currentColor"/><circle cx="21.5" cy="15" r="1" fill="currentColor"/><circle cx="25" cy="15" r="1" fill="currentColor"/></svg></span>
      <span class="contact__text">+00 000 000 0000</span>
    </div>
    <div class="contact contact--fax">
      <span class="contact__icon"><svg viewBox="0 0 30 26"><rect x="8" y="1" width="14" height="8" fill="#fff" stroke="currentColor" stroke-width="1.6"/><rect x="2" y="8" width="26" height="13" rx="3" fill="#fff" stroke="currentColor" stroke-width="1.6"/><rect x="7" y="15" width="16" height="10" fill="#fff" stroke="currentColor" stroke-width="1.6"/><path d="M10 18h10M10 21h10" stroke="currentColor" stroke-width="1.4"/></svg></span>
      <span class="contact__text">+00 000 000 0000</span>
    </div>
    <div class="contact contact--email">
      <span class="contact__icon"><span class="contact__at">@</span></span>
      <span class="contact__text">maren@maren-vickery.com</span>
    </div>

    <div class="seal seal--back" role="img" aria-label="Circular emblem"></div>
  </section>

</main>
</body>
</html>
```